Medical IT Business with New logo needs a fresh stationary design

First time on sketch Harbor; Thought I would give it a go.
This project is for business cards alone but we have loads of design work that needs to take place in the immediate future.

We provide IT services to the Medical Industry and value ourselves as offering a premium product to the market.

I am after a fresh, clean design using full colour 2 sided cards which includes our current colour palettes from our logo.

Card's must include:
- Logo
- Slogan
- Name
- Adress
- Email
- Phone
- Fax
- Mobile

Target Market(s)

Surgeons, High Profile Medical Personnel

Industry/Entity Type

Business

Fonts, CMYK Colours and Logo files attached.

Requirements
Must have
• Card's must include:
• - Logo
• - Slogan
• - Name
• - Adress
• - Email
• - Phone
• - Fax
• - Mobile
Nice to have
• Needs to incorporate our colour palette (attached CMYK colours)
Should not have
• Black backgrounds. Black text ok.

```html
<!DOCTYPE html>
<html lang="en">
<head>
<meta charset="utf-8">
<title>Clearpulse Systems – Business Card</title>
<link rel="stylesheet" href="https://fonts.googleapis.com/css2?family=Open+Sans:wght@400;600;700&display=swap">
<style>
  :root {
    --page-bg: #e6ecef;
    --card-white: #ffffff;
    --card-tint: #f6f8fa;
    --navy: #14409a;
    --brand-blue: #1a7fb5;
    --slogan-grey: #8a93a6;
    --panel-text: #ffffff;
  }
  * { box-sizing: border-box; margin: 0; padding: 0; }
  html, body { width: 1200px; height: 900px; overflow: hidden; }
  body {
    background: var(--page-bg);
    font-family: "Open Sans", Arial, sans-serif;
    display: flex;
    flex-direction: column;
    align-items: center;
    justify-content: center;
    gap: 44px;
  }
  .card {
    width: 600px;
    height: 343px;
    background: var(--card-white);
    box-shadow: 0 10px 30px rgba(20, 40, 70, 0.18);
    position: relative;
    overflow: hidden;
  }

  /* Brand name set as plain text */
  .brand-name {
    font-weight: 600;
    font-size: 32px;
    line-height: 1.1;
    color: var(--navy);
    white-space: nowrap;
  }
  .brand-slogan {
    font-size: 13px;
    color: var(--slogan-grey);
    margin-top: 4px;
    letter-spacing: 0.3px;
  }

  /* Back side */
  .card-back {
    display: flex;
    flex-direction: column;
    align-items: center;
    justify-content: center;
    text-align: center;
  }

  /* Front side */
  .card-front { background: var(--card-tint); }
  .card-front .brand { position: absolute; left: 48px; top: 100px; }
  .card-front .brand-name { font-size: 26px; }
  .card-front .brand-slogan { font-size: 12px; }

  .holder { position: absolute; left: 58px; top: 212px; }
  .holder-name { font-size: 26px; font-weight: 600; color: var(--navy); }
  .holder-name span { color: var(--brand-blue); }
  .holder-role { font-size: 19px; color: var(--navy); margin-top: 2px; }

  .contact-panel {
    position: absolute; right: 0; top: 0;
    width: 206px; height: 100%;
    background: var(--navy);
  }
  .contact-list {
    list-style: none;
    position: absolute;
    left: 408px;
    top: 48px;
  }
  .contact-item {
    display: flex; align-items: center; gap: 10px;
    color: var(--panel-text); font-size: 12.5px; line-height: 1.35;
    height: 48px;
  }
  .contact-icon {
    width: 30px; height: 30px; border-radius: 50%;
    border: 2px solid var(--panel-text);
    display: flex; align-items: center; justify-content: center; flex: none;
  }
  .contact-icon svg {
    width: 15px; height: 15px; fill: none;
    stroke: var(--panel-text); stroke-width: 1.8;
    stroke-linecap: round; stroke-linejoin: round;
  }
</style>
</head>
<body>

  <section class="card card-back" aria-label="Card back">
    <div class="brand">
      <div class="brand-name">Clearpulse Systems</div>
      <div class="brand-slogan">IT care for modern clinics</div>
    </div>
  </section>

  <section class="card card-front" aria-label="Card front">
    <div class="contact-panel"></div>

    <div class="brand">
      <div class="brand-name">Clearpulse Systems</div>
      <div class="brand-slogan">IT care for modern clinics</div>
    </div>

    <div class="holder">
      <div class="holder-name">Sam <span>Carter</span></div>
      <div class="holder-role">Director</div>
    </div>

    <ul class="contact-list">
      <li class="contact-item">
        <span class="contact-icon"><svg viewBox="0 0 16 16"><rect x="4.5" y="1.5" width="7" height="13" rx="1.5"/><line x1="7" y1="12" x2="9" y2="12"/></svg></span>
        0100 555 0147
      </li>
      <li class="contact-item">
        <span class="contact-icon"><svg viewBox="0 0 16 16"><path d="M2 6c0-2 2.5-3 6-3s6 1 6 3l-2.5 1L10 5.5H6L4.5 7z"/><rect x="3.5" y="8" width="9" height="5.5" rx="1"/></svg></span>
        0100 555 0148
      </li>
      <li class="contact-item">
        <span class="contact-icon"><svg viewBox="0 0 16 16"><rect x="2" y="6" width="12" height="7" rx="1"/><path d="M4.5 6V2h7v4"/><line x1="5" y1="10" x2="11" y2="10"/></svg></span>
        0100 555 0149
      </li>
      <li class="contact-item">
        <span class="contact-icon"><svg viewBox="0 0 16 16"><rect x="1.5" y="3.5" width="13" height="9" rx="1"/><path d="M1.5 4.5L8 9l6.5-4.5"/></svg></span>
        sam.carter@mail.test
      </li>
      <li class="contact-item">
        <span class="contact-icon"><svg viewBox="0 0 16 16"><path d="M8 14.5s-4.5-4.6-4.5-8a4.5 4.5 0 0 1 9 0c0 3.4-4.5 8-4.5 8z"/><circle cx="8" cy="6.5" r="1.6"/></svg></span>
        <span>12 Orchard Lane,<br>Fairview, NY 10000</span>
      </li>
    </ul>
  </section>

</body>
</html>
```